political advertisement for magazine

9.135 in 12.125 in. My wife is running for Judge. She needs an ad for an African-American Magazine ASAP . The ad is about a testimonial by one of her clients that makes her relatable to the African-American community. I am uploading the text for the testimonial, the picture of my wife and her client, her logo, a possible backdrop and also a slogan.

This is going in a church publication geared toward the African American Community

• The image of all the people in the back. On top of that image, you have "The people stand behind Lorena for Circuit Court Judge". Also you have a letter from her client with a picture of both of them. Also include the vote for Lorena logo and her headshot. The above is just my idea if you have an idea that is totally different but portrays that Lorena is for the people, I am ok with that too. thanks!

```html
<!DOCTYPE html>
<html lang="en">
<head>
<meta charset="utf-8">
<title>Lorena for Circuit Court Judge – Magazine Ad</title>
<link href="https://fonts.googleapis.com/css2?family=Cinzel:wght@600;700&family=Montserrat:wght@400;600;700&display=swap" rel="stylesheet">
<style>
  :root {
    --navy: #1f3b73;
    --navy-deep: #16295a;
    --red: #d3232b;
    --white: #ffffff;
    --paper: #eef0f3;
    --ink: #1d2340;
    --stage: #8e9196;
    --collage-a: #e6e2de;
    --collage-b: #d8d3cf;
  }
  * { box-sizing: border-box; margin: 0; padding: 0; }
  html, body { width: 1200px; height: 800px; overflow: hidden; }
  body {
    background: var(--stage);
    font-family: "Montserrat", Arial, sans-serif;
    position: relative;
  }
  .spread {
    position: absolute;
    top: 100px;
    left: 128px;
    display: flex;
    gap: 40px;
  }
  .page {
    position: relative;
    width: 452px;
    height: 600px;
    overflow: hidden;
    background: var(--paper);
  }
  .page__backdrop {
    position: absolute;
    inset: 0;
    background: linear-gradient(135deg, var(--collage-a), var(--collage-b) 50%, var(--collage-a));
    opacity: .85;
  }
  .page__shapes { position: absolute; inset: 0; width: 100%; height: 100%; }

  /* Testimonial page */
  .testimonial__title {
    position: absolute;
    top: 124px;
    left: 0; right: 0;
    padding-left: 60px;
    text-align: center;
    font-family: "Cinzel", Georgia, serif;
    font-weight: 700;
    font-size: 33px;
    letter-spacing: .5px;
    color: var(--navy-deep);
  }
  .testimonial__photo {
    position: absolute;
    left: 41px; top: 186px;
    width: 152px; height: 307px;
    background: linear-gradient(180deg, #4f7a44 0%, #6e8f5a 35%, #b9b3aa 70%, #8fa2b8 100%);
  }
  .testimonial__letter {
    position: absolute;
    left: 202px; top: 183px;
    width: 190px;
    font-size: 10.6px;
    line-height: 1.36;
    color: var(--ink);
  }
  .testimonial__letter p + p { margin-top: 6px; }
  .testimonial__signoff { margin-top: 8px; font-weight: 700; line-height: 1.4; }
  .testimonial__signoff .closing { color: var(--red); display: block; }
  .testimonial__signoff .name { color: var(--navy); display: block; }
  .disclaimer {
    position: absolute;
    left: 30px; right: 30px; top: 526px;
    text-align: center;
    font-size: 8.6px;
    line-height: 1.45;
    color: var(--ink);
    padding-bottom: 6px;
    border-bottom: 1px solid var(--navy);
  }
  .disclaimer .committee { color: var(--navy); font-weight: 700; }
  .disclaimer .office { color: var(--red); font-weight: 700; }

  /* Cover page */
  .campaign-name {
    position: absolute;
    top: 18px; left: 36px;
    font-family: "Cinzel", Georgia, serif;
    font-weight: 700;
    color: var(--red);
    line-height: 1.05;
  }
  .campaign-name .line-vote { display: block; font-size: 28px; }
  .campaign-name .line-first { display: block; font-size: 54px; }
  .campaign-name .line-last { display: block; font-size: 15px; letter-spacing: 3px; padding-left: 16px; margin-top: 4px; }
  .campaign-name .line-office { display: block; font-size: 30px; padding-left: 36px; margin-top: 4px; }
  .headshot {
    position: absolute;
    left: 176px; top: 230px;
    width: 176px; height: 176px;
    border-radius: 50%;
    background: radial-gradient(circle at 50% 38%, #c9a58e 0%, #8a6a58 40%, #2a2a30 75%);
  }
  .slogan {
    position: absolute;
    right: 22px; top: 486px;
    text-align: right;
    font-family: "Cinzel", Georgia, serif;
    font-weight: 600;
    color: var(--white);
    line-height: 1.1;
  }
  .slogan .lead { display: block; font-size: 17px; letter-spacing: .5px; }
  .slogan .candidate { display: block; font-size: 38px; }
  .slogan .office { display: block; font-size: 21px; }
</style>
</head>
<body>
  <main class="spread">
    <!-- Testimonial page -->
    <section class="page testimonial">
      <div class="page__backdrop" role="img" aria-label="Soft collage of portraits of community members"></div>
      <svg class="page__shapes" viewBox="0 0 452 600" aria-hidden="true">
        <path d="M0 0 H232 C150 30 60 90 28 170 C18 195 14 212 12 228 L0 222 Z" fill="var(--navy)"/>
        <path d="M232 0 C150 30 60 90 28 170 C18 195 14 212 12 228" fill="none" stroke="var(--white)" stroke-width="10"/>
        <path d="M226 0 C146 32 56 92 24 172 C14 198 10 214 8 230 L22 232" fill="none" stroke="var(--red)" stroke-width="6"/>
      </svg>
      <h1 class="testimonial__title">Testimonial</h1>
      <div class="testimonial__photo" role="img" aria-label="Photo of Lorena shaking hands with her client in front of a flowering garden"></div>
      <div class="testimonial__letter">
        <p>For the past few years, Lorena Castellano Reyes has been my lawyer. She has always strived to provide excellence in legal services. Her almost encyclopedic knowledge of the law makes for a flawless, precise, navigation of the legal system, with results.</p>
        <p>She is the epitome of professionalism, that is aptly balanced by her calm persona. Her empathy is more than commendable, and her legal experience unmatched. Lorena Castellano Reyes is truly one of kind, deserving of all accolades, appointments, and accomplishments.</p>
        <p class="testimonial__signoff"><span class="closing">Yours Truly,</span><span class="name">Daniel Whitfield</span></p>
      </div>
      <p class="disclaimer">Political Advertisement paid for and approved by the Committee to<br><span class="committee">Elect Lorena Castellano Reyes,</span><br>no party affiliation, for <span class="office">Circuit Court Judge</span></p>
    </section>

    <!-- Cover page -->
    <section class="page cover">
      <div class="page__backdrop" role="img" aria-label="Soft collage of portraits of community members"></div>
      <svg class="page__shapes" viewBox="0 0 452 600" aria-hidden="true">
        <path d="M20 600 C40 500 110 430 210 420 C330 408 410 340 452 190 L452 600 Z" fill="var(--navy)"/>
        <path d="M8 600 C28 495 100 425 205 412 C325 398 405 330 448 178" fill="none" stroke="var(--white)" stroke-width="9"/>
        <path d="M2 600 C22 490 94 420 200 406" fill="none" stroke="var(--red)" stroke-width="6"/>
        <path d="M372 218 C400 190 420 160 426 140 C440 170 436 220 410 262 Z" fill="var(--red)"/>
        <circle cx="264" cy="318" r="102" fill="var(--red)"/>
        <circle cx="264" cy="318" r="93" fill="var(--white)"/>
      </svg>
      <div class="campaign-name">
        <span class="line-vote">Vote</span>
        <span class="line-first">Lorena</span>
        <span class="line-last">Castellano Reyes</span>
        <span class="line-office">For Judge</span>
      </div>
      <div class="headshot" role="img" aria-label="Headshot of Lorena in a dark blazer"></div>
      <p class="slogan">
        <span class="lead">The People Stand Behind</span>
        <span class="candidate">Lorena For</span>
        <span class="office">Circuit Court Judge”.</span>
      </p>
    </section>
  </main>
</body>
</html>
```